Real Estate For Sale Sign

I need to design a for sale sign. It needs to include The following information
Logo: Attached
Name: Corinne Vasquel,
Company Name: Gilded Harbor Real Estate,
Phone Number: 503-841-2096
BRE Licence Number 04817359 (Can Be small)
Sign size 24x30

I am not sure about including my website but I would like to see options with it. www.gildedharbor-example.com
Updates

Target Market(s)

Potential Buyers or Sellers of Real Estate. Must be easy to read.

Industry/Entity Type

Real Estate

Requirements
Must have
• I want it to feel luxurious and sharp.

```html
<!DOCTYPE html>
<html lang="en">
<head>
<meta charset="utf-8">
<title>Gilded Harbor Real Estate – For Sale Sign</title>
<link rel="stylesheet" href="https://fonts.googleapis.com/css2?family=Arimo:wght@400;700&family=Cinzel:wght@400;600&family=Crimson+Pro:wght@400&family=Inter:wght@300;700&display=swap">
<style>
  :root {
    --page: #ffffff;
    --label: #111111;
    --sign-dark: #000000;
    --sign-light: #ffffff;
    --sign-edge: #d4d4d4;
    --accent-cyan: #3bb5e8;
    --brand-blue: #2a62ae;
    --phone-light: #ffffff;
    --phone-dark: #454545;
    --web-grey: #6e6e6e;
    --web-grey-dark: #555555;
    --licence-dark: #e8e8e8;
    --licence-light: #2b2b5a;
    --scene-sky: #c9d3cf;
    --scene-trees: #2f4330;
    --scene-lawn: #4f7a3a;
  }
  * { box-sizing: border-box; margin: 0; padding: 0; }
  html, body { width: 1200px; height: 1000px; overflow: hidden; background: var(--page); }
  .board { position: relative; width: 1200px; height: 1000px; }

  .caption {
    position: absolute;
    font-family: "Arimo", Arial, sans-serif;
    font-weight: 700;
    font-size: 11.5px;
    color: var(--label);
  }

  .sign {
    position: absolute;
    width: 446px;
    height: 557px;
    border: 3px solid var(--sign-edge);
    box-shadow: 2px 4px 6px rgba(0,0,0,0.35);
    text-align: center;
    overflow: hidden;
  }
  .sign--dark { left: 134px; top: 69px; background: var(--sign-dark); }
  .sign--light { left: 648px; top: 69px; background: var(--sign-light); }

  .sign__mark { position: absolute; left: 50%; top: 28px; transform: translateX(-50%); }

  .sign__brand {
    position: absolute; left: 0; right: 0; top: 174px;
    font-family: "Cinzel", serif;
    font-weight: 400;
    color: var(--brand-blue);
    line-height: 1;
  }
  .sign__brand-name { display: block; font-size: 34px; letter-spacing: 0.5px; }
  .sign__brand-sub { display: block; font-size: 17px; letter-spacing: 5px; margin-top: 6px; }

  .sign__headline {
    position: absolute; left: 0; right: 0; top: 252px;
    font-family: "Inter", Helvetica, sans-serif;
    color: var(--accent-cyan);
    line-height: 0.86;
  }
  .sign__headline-for { display: block; font-weight: 300; font-size: 88px; letter-spacing: -1px; }
  .sign__headline-sale { display: block; font-weight: 700; font-size: 88px; letter-spacing: -2px; }

  .sign__agent {
    position: absolute; left: 0; right: 0; top: 444px;
    font-family: "Cinzel", serif; font-weight: 600;
    font-size: 21px; letter-spacing: 1px;
    color: var(--brand-blue); line-height: 1;
  }
  .sign__phone {
    position: absolute; left: 0; right: 0; top: 460px;
    font-family: "Crimson Pro", serif; font-weight: 400;
    font-size: 50px; line-height: 1;
  }
  .sign--dark .sign__phone { color: var(--phone-light); }
  .sign--light .sign__phone { color: var(--phone-dark); }

  .sign__web {
    position: absolute; left: 0; right: 0; top: 508px;
    font-family: "Arimo", Arial, sans-serif; font-weight: 700;
    font-size: 18px; line-height: 1;
  }
  .sign--dark .sign__web { color: var(--web-grey); }
  .sign--light .sign__web { color: var(--web-grey-dark); }

  .sign__licence {
    position: absolute; right: 92px; top: 528px;
    font-family: "Arimo", Arial, sans-serif; font-weight: 700;
    font-size: 5.5px; line-height: 1;
  }
  .sign--dark .sign__licence { color: var(--licence-dark); }
  .sign--light .sign__licence { color: var(--licence-light); }

  .placement {
    position: absolute; top: 651px; width: 370px; height: 270px;
    background:
      linear-gradient(180deg, var(--scene-sky) 0%, var(--scene-trees) 8%, var(--scene-trees) 55%, var(--scene-lawn) 62%, var(--scene-lawn) 100%);
  }
  .placement--dark { left: 188px; }
  .placement--light { left: 651px; }
</style>
</head>
<body>
<main class="board">

  <p class="caption" style="left:136px; top:45px;">For Sale Sign (Black Background)</p>
  <p class="caption" style="left:649px; top:45px;">For Sale Sign (White Background)</p>

  <section class="sign sign--dark" aria-label="For sale sign, black background">
    <svg class="sign__mark" width="120" height="120" viewBox="0 0 120 120" aria-hidden="true">
      <circle cx="60" cy="60" r="54" fill="none" stroke="var(--brand-blue)" stroke-width="6"/>
    </svg>
    <h2 class="sign__brand">
      <span class="sign__brand-name">GILDED HARBOR</span>
      <span class="sign__brand-sub">REAL ESTATE</span>
    </h2>
    <h1 class="sign__headline">
      <span class="sign__headline-for">FOR</span>
      <span class="sign__headline-sale">SALE</span>
    </h1>
    <p class="sign__agent">Corinne Vasquel</p>
    <p class="sign__phone">503-841-2096</p>
    <p class="sign__web">www.gildedharbor-example.com</p>
    <p class="sign__licence">BRE Licence Number 04817359</p>
  </section>

  <section class="sign sign--light" aria-label="For sale sign, white background">
    <svg class="sign__mark" width="120" height="120" viewBox="0 0 120 120" aria-hidden="true">
      <circle cx="60" cy="60" r="54" fill="none" stroke="var(--brand-blue)" stroke-width="6"/>
    </svg>
    <h2 class="sign__brand">
      <span class="sign__brand-name">GILDED HARBOR</span>
      <span class="sign__brand-sub">REAL ESTATE</span>
    </h2>
    <h1 class="sign__headline">
      <span class="sign__headline-for">FOR</span>
      <span class="sign__headline-sale">SALE</span>
    </h1>
    <p class="sign__agent">Corinne Vasquel</p>
    <p class="sign__phone">503-841-2096</p>
    <p class="sign__web">www.gildedharbor-example.com</p>
    <p class="sign__licence">BRE Licence Number 04817359</p>
  </section>

  <div class="placement placement--dark" role="img" aria-label="Photo of the black sign hanging from a white yard post in front of a house with a lawn"></div>
  <div class="placement placement--light" role="img" aria-label="Photo of the white sign hanging from a white yard post in front of a house with a lawn"></div>

  <p class="caption" style="left:188px; top:933px;">For Sale Sign Black Positioning Reference</p>
  <p class="caption" style="left:651px; top:933px;">For Sale Sign White Positioning Reference</p>

</main>
</body>
</html>
```